Folded Business Cards for Guarantee, Layaway & The Fine Print

I am looking for a set of (3) folded business for our guarantee, layaway and fine print policies. I would like the same design for each of these cards, with the exception of the picture, title and verbiage.
The front of each card must include our logo, the title of the card (Our Guarantee, Layaway or The Fine Print,) and a picture of a piece of jewelry. The inside of the card should state our policies. The back of the card should have our logo, address (Bellstone Court #9, Marlow Glen, NH 03991,) phone # (555-281-0947) email & web address (info@vantorgems.com, www.vantorgems.com) and social media icons (FB, Twitter, Pinterest, Instagram)

The layaway card needs a place for the customer's signature.

I was thinking the orientation of the card should be vertical but if the right design ends up being horizontal, I'm ok with that. I do have concerns about readability and that this may be too much information for a folded business card. So, I am open to either changing the front & back, if need be or going to a different format (standard postcard size. Verbiage may also need to be trimmed down, but I need to know what is possible first.

Our branding colors are espresso brown & coppery orange so please do not stray from this color palette. The font of our logo is joefin. I would like the verbiage of the cards to be in quattrocento sans font. We would like a modern & clean look please.

Attached, please find our logo, policies and jewelry pictures. For picture placement, please do the following: Layaway Card (Quartz & onyx pendant,) The Fine Print Card (Orange Garnet Pendant,) Our Guarantee (triple Green Tourmaline Ring.)

```html
<!DOCTYPE html>
<html lang="en">
<head>
<meta charset="utf-8">
<title>Vantor – Our Guarantee folded card</title>
<link rel="stylesheet" href="https://fonts.googleapis.com/css2?family=Open+Sans:wght@600&family=Quattrocento+Sans:wght@400;700&display=swap">
<style>
  :root {
    --espresso: #2a1a14;
    --espresso-deep: #1f130e;
    --paper: #f1efee;
    --paper-shade: #dcd9d7;
    --ink: #2b2220;
    --cream: #f4efe9;
    --stage: #ffffff;
  }
  * { box-sizing: border-box; margin: 0; padding: 0; }
  html, body { width: 1200px; height: 900px; overflow: hidden; background: var(--stage); }
  .canvas { position: relative; width: 1200px; height: 900px; }

  .spread { position: absolute; top: 130px; width: 500px; height: 640px; display: flex; box-shadow: 0 6px 18px rgba(0,0,0,.12); }
  .spread--outside { left: 70px; }
  .spread--inside { left: 630px; }

  .panel { position: relative; width: 250px; height: 640px; }

  /* outside */
  .panel--back, .panel--front { background: var(--espresso); color: var(--cream); font-family: "Quattrocento Sans", sans-serif; }
  .panel--back { border-right: 1px solid var(--espresso-deep); }
  .brand { position: absolute; top: 70px; left: 40px; color: var(--cream); font-weight: 400; }
  .brand__name { font-size: 50px; letter-spacing: 3px; line-height: 1; }
  .brand__tag { font-size: 15px; letter-spacing: 1px; margin-top: 6px; margin-left: 2px; }

  .contact { position: absolute; top: 215px; left: 28px; list-style: none; font-size: 17px; line-height: 1.3; }
  .contact li { display: flex; gap: 8px; margin-bottom: 18px; }
  .contact svg { flex: none; width: 18px; height: 18px; margin-top: 2px; fill: var(--cream); }
  .contact .address span { display: block; }
  .contact .address .indent { padding-left: 40px; }

  .social { position: absolute; bottom: 88px; left: 0; right: 0; display: flex; justify-content: center; gap: 7px; }
  .social span { width: 22px; height: 22px; border-radius: 4px; background: var(--cream); }
  .web { position: absolute; bottom: 52px; left: 0; right: 0; text-align: center; font-size: 16px; }

  .card-title { position: absolute; top: 92px; left: 0; right: 0; text-align: center; font-family: "Open Sans", sans-serif; font-weight: 600; font-size: 28px; color: #fff; }
  .product-photo { position: absolute; top: 240px; left: 58px; width: 134px; height: 270px; border-radius: 10px;
    background: radial-gradient(ellipse at 50% 50%, #3f4a1e 0%, #6b5522 40%, #4a3a25 70%, var(--espresso) 100%); }

  /* inside */
  .panel--left, .panel--right { background: var(--paper); color: var(--ink); font-family: "Quattrocento Sans", sans-serif; font-size: 15px; line-height: 1.42; }
  .panel--left { background: linear-gradient(to right, var(--paper) 85%, var(--paper-shade)); }
  .panel--right { background: linear-gradient(to right, var(--paper-shade), var(--paper) 15%); }
  .band { position: absolute; top: 40px; left: 0; right: 0; height: 56px; background: var(--espresso); }
  .band__title { color: var(--cream); font-size: 19px; font-weight: 400; padding: 15px 0 0 10px; }

  .policy { position: absolute; top: 132px; left: 10px; right: 8px; }
  .policy p { margin-bottom: 28px; }
  .panel--right .policy { top: 108px; left: 16px; right: 8px; }
</style>
</head>
<body>
<main class="canvas">

  <section class="spread spread--outside" aria-label="Card outside">
    <div class="panel panel--back">
      <div class="brand">
        <div class="brand__name">vantor</div>
        <div class="brand__tag">Jewelry &amp; Design Studio</div>
      </div>
      <ul class="contact">
        <li class="address">
          <svg viewBox="0 0 20 20" aria-hidden="true"><path d="M10 2 1 10h3v8h5v-5h2v5h5v-8h3z"/></svg>
          <div><span>Bellstone Court #9,</span><span class="indent">Marlow Glen,</span><span class="indent">NH 03991.</span></div>
        </li>
        <li>
          <svg viewBox="0 0 20 20" aria-hidden="true"><path d="M5 1 8 5 6 8c1 2 4 5 6 6l3-2 4 3-2 4C10 19 1 10 1 3z"/></svg>
          <span>555-281-0947</span>
        </li>
        <li>
          <svg viewBox="0 0 20 20" aria-hidden="true"><path d="M1 4h18v12H1zm2 1.5v9h14v-9l-7 5z M3.5 5 10 9.5 16.5 5z" fill-rule="evenodd"/></svg>
          <span>info@vantorgems.com</span>
        </li>
      </ul>
      <div class="social" aria-label="Social media links"><span></span><span></span><span></span><span></span></div>
      <div class="web">www.vantorgems.com</div>
    </div>
    <div class="panel panel--front">
      <h1 class="card-title">Our Guarantee</h1>
      <div class="product-photo" role="img" aria-label="Photo of a triple green tourmaline ring in gold and oxidized silver"></div>
    </div>
  </section>

  <section class="spread spread--inside" aria-label="Card inside">
    <div class="panel panel--left">
      <div class="band"><h2 class="band__title">Our Promise to You...</h2></div>
      <div class="policy">
        <p>Vantor's guarantees your jewelry purchase for 2 years from date of purchase.</p>
        <p>We will repair or replace any piece of jewelry that is determined to be defective in materials and/or workmanship.</p>
        <p>We will repair or replace any stone loss up to 0.20ct. per stone, due to defects in materials and/or workmanship.</p>
        <p>Our jewelry repairs are guaranteed for 6 months from completion date.</p>
      </div>
    </div>
    <div class="panel panel--right">
      <div class="band"></div>
      <div class="policy">
        <p>Our watch repairs are guaranteed for 90 days from completion date. We do not warranty watches against water damage.</p>
        <p>We offer free lifetime cleaning &amp; inspection of your jewelry from Vantor's. We'll make sure everything is safe &amp; secure and, of course, sparkling. You should do this at least every six months.</p>
        <p>Above all, we want you to be pleased with your jewelry purchase or repair from Vantor's. If you have any questions or concerns, please never hesitate to speak to us.</p>
      </div>
    </div>
  </section>

</main>
</body>
</html>
```